Grotto's Showdown

Countrywide Spotlight-like competition for 17 and older contestants
Preliminaries May 2nd, 9th, 16th, finals are May 27th and may 28th

Grotto's is a music room/nightclub in downtown Napa, CA

$15 entry fee for finals

Preliminaries 7 - 10pm
Finals - 4 - 8 pm

music/caricatures/instruments/etc

Target Market(s)

age 17 - 55

```html
<!DOCTYPE html>
<html lang="en">
<head>
<meta charset="utf-8">
<title>Grotto's Showdown</title>
<link href="https://fonts.googleapis.com/css2?family=Audiowide&family=Michroma&family=Russo+One&display=swap" rel="stylesheet">
<style>
  :root {
    --night: #12060d;
    --wine: #7a0d1e;
    --crimson: #b3172b;
    --teal: #1e6f78;
    --glow: #ffffff;
    --signal-red: #e3352b;
    --title-blue: #2f86bf;
    --title-blue-light: #8cc6e8;
    --caption: #c9dbea;
    --ink: #ffffff;
  }
  html, body {
    margin: 0;
    padding: 0;
    overflow: hidden;
    background: var(--night);
  }
  .poster {
    position: relative;
    width: 926px;
    height: 1200px;
    overflow: hidden;
    background: var(--night);
    font-family: "Michroma", sans-serif;
    color: var(--ink);
  }
  .backdrop {
    position: absolute;
    inset: 0;
    background:
      radial-gradient(ellipse 520px 300px at 460px 600px, rgba(255,255,255,0.98) 0%, rgba(255,255,255,0.9) 45%, rgba(255,255,255,0) 100%),
      radial-gradient(ellipse 700px 260px at 460px 380px, rgba(255,235,240,0.85) 0%, rgba(255,220,225,0) 100%),
      radial-gradient(ellipse 620px 240px at 460px 820px, rgba(255,245,230,0.9) 0%, rgba(255,200,120,0.35) 55%, rgba(255,150,80,0) 100%),
      radial-gradient(ellipse 420px 320px at 90px 140px, rgba(30,111,120,0.85) 0%, rgba(30,111,120,0) 100%),
      radial-gradient(ellipse 520px 380px at 820px 260px, rgba(179,23,43,0.8) 0%, rgba(179,23,43,0) 100%),
      radial-gradient(ellipse 560px 300px at 120px 1040px, rgba(179,23,43,0.75) 0%, rgba(179,23,43,0) 100%),
      linear-gradient(180deg, #1a0a14 0%, var(--wine) 40%, var(--wine) 70%, #3a0714 100%);
  }
  .brand {
    position: absolute;
    left: 41px;
    top: 12px;
    width: 203px;
    height: 76px;
    background: var(--glow);
    display: flex;
    align-items: center;
    justify-content: center;
  }
  .brand-name {
    font-family: "Michroma", sans-serif;
    font-size: 28px;
    color: var(--crimson);
    letter-spacing: 1px;
  }
  .site {
    position: absolute;
    right: 34px;
    top: 26px;
    font-family: "Russo One", sans-serif;
    font-size: 24px;
    letter-spacing: 1px;
  }
  .venue-name {
    position: absolute;
    top: 112px;
    width: 100%;
    text-align: center;
    font-family: "Audiowide", sans-serif;
    font-size: 38px;
    color: var(--signal-red);
    letter-spacing: 2px;
  }
  .venue-desc {
    position: absolute;
    top: 165px;
    width: 100%;
    text-align: center;
    font-family: "Audiowide", sans-serif;
    font-size: 33px;
    letter-spacing: 2px;
  }
  .title {
    position: absolute;
    left: 0;
    width: 100%;
    text-align: center;
    font-family: "Audiowide", sans-serif;
    text-transform: uppercase;
    background: linear-gradient(180deg, var(--title-blue-light) 0%, var(--title-blue) 45%, #1f6a9c 100%);
    -webkit-background-clip: text;
    background-clip: text;
    color: transparent;
    line-height: 1;
    margin: 0;
  }
  .title-top { top: 420px; font-size: 118px; letter-spacing: 6px; }
  .title-bottom { top: 620px; font-size: 104px; letter-spacing: 2px; }
  .location {
    position: absolute;
    top: 910px;
    width: 100%;
    text-align: center;
    font-family: "Audiowide", sans-serif;
    font-size: 44px;
    letter-spacing: 3px;
    color: var(--caption);
    text-shadow: 0 0 6px rgba(40,90,140,0.6);
  }
  .schedule {
    position: absolute;
    left: 12px;
    top: 1040px;
    width: 820px;
    font-family: "Russo One", sans-serif;
    font-size: 30px;
    letter-spacing: 0.5px;
  }
  .schedule-row {
    display: flex;
    justify-content: space-between;
    height: 52px;
    align-items: center;
  }
  .schedule-row .time { width: 170px; text-align: left; }
  .fee {
    position: absolute;
    left: 12px;
    top: 1146px;
    font-family: "Russo One", sans-serif;
    font-size: 30px;
    letter-spacing: 0.5px;
  }
</style>
</head>
<body>
<main class="poster">
  <div class="backdrop" role="img" aria-label="Fireworks bursting over a wall of bright stage lights on a dark red and teal background"></div>

  <div class="brand"><span class="brand-name">GROTTO'S</span></div>
  <div class="site">WWW.GROTTOSNAPA.COM</div>

  <div class="venue-name">GROTTO'S</div>
  <div class="venue-desc">IS A MUSIC ROOM/NIGHTCLUB</div>

  <h1 class="title title-top">Grotto's</h1>
  <h1 class="title title-bottom">Showdown</h1>

  <div class="location">IN DOWNTOWN NAPA CA</div>

  <div class="schedule">
    <div class="schedule-row"><span>PRELIMINARIES MAY 2ND 9TH, 16TH</span><span class="time">7-10 PM</span></div>
    <div class="schedule-row"><span>FINALS MAY 27TH-28TH</span><span class="time">4-8 PM</span></div>
  </div>
  <div class="fee">$15 ENTRY FEE FOR FINALS</div>
</main>
</body>
</html>
```